Brochure Design Project

Please design a corporate brochure for my business "Corvin Asbestos & Safety"

Specs:-
- A4 flat size, three panel front, three panel back, roll-folded to DL
- Portrait orientation
- Full colour
Updates

Please don't forget to send in your designs. I believe the competition ends in a few hours. Thank you!

Target Market(s)

Business owners, commercial/industrial building owners, real estate property managers, strata managers

Industry/Entity Type

Business

Requirements
Must have
• - Professional / modern but serious as the content is important
- Cover page in particular must stand out so it will be noticeable if sitting on someone's desk
- Good use of whitespace and not too crowded
- Heading highlighted in warm/hot colour i.e. burnt orange, all other text in black
- Font Georgia 11pt
Nice to have
• - I have uploaded our letterhead source files too - please weave in the theme/look and feel of the letterhead into the brochure if possible.

```html
<!DOCTYPE html>
<html lang="en">
<head>
<meta charset="utf-8">
<title>Corvin Asbestos &amp; Safety – Asbestos Compliance Brochure</title>
<link rel="stylesheet" href="https://fonts.googleapis.com/css2?family=Anton&family=Gelasio:wght@400;700&display=swap">
<style>
  :root {
    --warning-yellow: #ece41f;
    --ink: #1a1a1a;
    --paper: #eeeeee;
    --paper-light: #f6f6f6;
    --burnt-orange: #f38f1c;
    --leaf-green: #7dc14b;
    --navy: #2e2c54;
    --white: #ffffff;
    --illustration-light: #f5f3f5;
    --illustration-mid: #e9dfe6;
  }
  * { box-sizing: border-box; margin: 0; padding: 0; }
  html, body { width: 1200px; height: 845px; overflow: hidden; }
  body { background: var(--white); }

  .spread {
    position: relative;
    width: 1200px;
    height: 845px;
    overflow: hidden;
    background: linear-gradient(160deg, var(--paper-light), var(--paper) 60%, #e6e6e6);
    font-family: Georgia, "Gelasio", serif;
    color: var(--ink);
  }

  /* warning strip */
  .warning-strip {
    position: absolute; left: 0; top: 0; width: 1200px; height: 55px;
    background: var(--warning-yellow);
    display: flex; justify-content: space-around; align-items: center;
    padding: 0 10px;
  }
  .warning-sign { display: flex; align-items: center; gap: 6px; }
  .warning-sign svg { width: 40px; height: 36px; }
  .warning-sign span {
    font-family: "Anton", "Arial Narrow", sans-serif;
    font-size: 14px; line-height: 14px; text-align: center; color: var(--ink);
    letter-spacing: 0.2px;
  }

  /* shared */
  .panel-heading-shape { position: absolute; top: 0; left: 0; }
  .body-copy p {
    font-size: 17px; line-height: 25.7px; text-align: justify; margin-bottom: 25.7px;
  }
  .body-copy p.tight { margin-bottom: 0; }

  /* left panel */
  .illustration {
    position: absolute; left: 21px; top: 84px; width: 355px; height: 266px;
    background: linear-gradient(180deg, var(--illustration-light), var(--illustration-mid));
  }
  .danger-heading {
    position: absolute; left: 0; top: 385px; width: 379px; height: 52px;
    background: var(--burnt-orange);
    font-family: "Anton", "Arial Narrow", sans-serif; font-weight: 400;
    color: var(--white); font-size: 24px; line-height: 52px;
    padding-left: 38px; letter-spacing: 0.2px;
  }
  .left-copy { position: absolute; left: 36px; top: 440px; width: 340px; }

  /* middle panel */
  .middle-heading {
    position: absolute; left: 446px; top: 66px; width: 350px;
    font-family: "Anton", "Arial Narrow", sans-serif; font-weight: 400; color: var(--white);
    font-size: 22px; line-height: 28.5px;
  }
  .middle-heading .lead { display: block; font-size: 40px; line-height: 48px; }
  .middle-copy { position: absolute; left: 417px; top: 290px; width: 362px; }
  .fines-callout {
    position: absolute; left: 626px; top: 718px; width: 152px; text-align: center;
    font-weight: 700; font-size: 13px; line-height: 14px; white-space: nowrap;
  }
  .fines-callout strong {
    display: block; color: var(--burnt-orange); font-size: 21px; line-height: 24px;
  }

  /* right panel */
  .right-heading {
    position: absolute; left: 838px; top: 62px; width: 350px;
    font-family: "Anton", "Arial Narrow", sans-serif; font-weight: 400; color: var(--white);
    font-size: 22px; line-height: 28.5px;
  }
  .right-heading .lead { display: block; font-size: 38px; line-height: 44px; }
  .right-copy { position: absolute; left: 818px; top: 338px; width: 340px; }

  /* foot band */
  .foot-band { position: absolute; left: 0; bottom: 0; }
</style>
</head>
<body>
<main class="spread">

  <header class="warning-strip">
    <div class="warning-sign"><svg viewBox="0 0 40 36" aria-hidden="true"><path d="M20 3 L37 33 L3 33 Z" fill="none" stroke="#1a1a1a" stroke-width="3" stroke-linejoin="round"/><rect x="18.4" y="13" width="3.2" height="11" fill="#1a1a1a"/><circle cx="20" cy="28" r="1.9" fill="#1a1a1a"/></svg><span>DANGER<br>ASBESTOS</span></div>
    <div class="warning-sign"><svg viewBox="0 0 40 36" aria-hidden="true"><path d="M20 3 L37 33 L3 33 Z" fill="none" stroke="#1a1a1a" stroke-width="3" stroke-linejoin="round"/><rect x="18.4" y="13" width="3.2" height="11" fill="#1a1a1a"/><circle cx="20" cy="28" r="1.9" fill="#1a1a1a"/></svg><span>DANGER<br>ASBESTOS</span></div>
    <div class="warning-sign"><svg viewBox="0 0 40 36" aria-hidden="true"><path d="M20 3 L37 33 L3 33 Z" fill="none" stroke="#1a1a1a" stroke-width="3" stroke-linejoin="round"/><rect x="18.4" y="13" width="3.2" height="11" fill="#1a1a1a"/><circle cx="20" cy="28" r="1.9" fill="#1a1a1a"/></svg><span>DANGER<br>ASBESTOS</span></div>
    <div class="warning-sign"><svg viewBox="0 0 40 36" aria-hidden="true"><path d="M20 3 L37 33 L3 33 Z" fill="none" stroke="#1a1a1a" stroke-width="3" stroke-linejoin="round"/><rect x="18.4" y="13" width="3.2" height="11" fill="#1a1a1a"/><circle cx="20" cy="28" r="1.9" fill="#1a1a1a"/></svg><span>DANGER<br>ASBESTOS</span></div>
    <div class="warning-sign"><svg viewBox="0 0 40 36" aria-hidden="true"><path d="M20 3 L37 33 L3 33 Z" fill="none" stroke="#1a1a1a" stroke-width="3" stroke-linejoin="round"/><rect x="18.4" y="13" width="3.2" height="11" fill="#1a1a1a"/><circle cx="20" cy="28" r="1.9" fill="#1a1a1a"/></svg><span>DANGER<br>ASBESTOS</span></div>
    <div class="warning-sign"><svg viewBox="0 0 40 36" aria-hidden="true"><path d="M20 3 L37 33 L3 33 Z" fill="none" stroke="#1a1a1a" stroke-width="3" stroke-linejoin="round"/><rect x="18.4" y="13" width="3.2" height="11" fill="#1a1a1a"/><circle cx="20" cy="28" r="1.9" fill="#1a1a1a"/></svg><span>DANGER<br>ASBESTOS</span></div>
    <div class="warning-sign"><svg viewBox="0 0 40 36" aria-hidden="true"><path d="M20 3 L37 33 L3 33 Z" fill="none" stroke="#1a1a1a" stroke-width="3" stroke-linejoin="round"/><rect x="18.4" y="13" width="3.2" height="11" fill="#1a1a1a"/><circle cx="20" cy="28" r="1.9" fill="#1a1a1a"/></svg><span>DANGER<br>ASBESTOS</span></div>
    <div class="warning-sign"><svg viewBox="0 0 40 36" aria-hidden="true"><path d="M20 3 L37 33 L3 33 Z" fill="none" stroke="#1a1a1a" stroke-width="3" stroke-linejoin="round"/><rect x="18.4" y="13" width="3.2" height="11" fill="#1a1a1a"/><circle cx="20" cy="28" r="1.9" fill="#1a1a1a"/></svg><span>DANGER<br>ASBESTOS</span></div>
  </header>

  <svg class="panel-heading-shape" width="1200" height="845" viewBox="0 0 1200 845" aria-hidden="true">
    <polygon points="398,59 800,59 800,140 457,276 398,152" fill="var(--leaf-green)"/>
    <polygon points="800,59 1200,59 1200,200 885,319 800,279" fill="var(--navy)"/>
  </svg>

  <!-- panel: why asbestos is dangerous -->
  <section class="panel panel-danger">
    <div class="illustration" role="img" aria-label="Medical illustration of pleural mesothelioma: lungs with asbestos fibres lodged in the mesothelial tissue and a magnified view of diseased cells"></div>
    <h2 class="danger-heading">Why is Asbestos so dangerous?</h2>
    <div class="body-copy left-copy">
      <p>Asbestos is a hazardous substance that poses a risk to health by inhalation if the asbestos fibres become airborne. Exposure to these fibres is known to cause mesothelioma, asbestosis and lung cancer.</p>
      <p class="tight">Australia had the highest per capita use of asbestos in the world in the 1950s and it is not surprising that it has the world’s highest incidence of asbestos related cancer. Asbestos has caused a significant death toll and much suffering in Australia, and the impact of asbestos-related diseases is expected to peak in 2020.</p>
    </div>
  </section>

  <!-- panel: compliance -->
  <section class="panel panel-compliance">
    <h2 class="middle-heading"><span class="lead">Are you</span>compliant with current<br>Work Health and Safety (WHS)<br>legislation regarding<br>Asbestos?</h2>
    <div class="body-copy middle-copy">
      <p>The Work Health and Safety (WHS) Act (2011) requires that a person conducting a business or undertaking (PCBU) must ensure, as far as reasonably practicable, the health and safety of their workers.</p>
      <p class="tight">Further, the Work Health and Safety (WHS) Regulation (2011) and its associated Code of Practice – How to Manage and Control Asbestos in the Workplace requires the person with management or control of a workplace to ensure, so far as is reasonably practicable, that all asbestos at the workplace is identified.</p>
      <p class="tight" style="text-align:left">This applies to all non-domestic buildings constructed prior to 31st December 2003 – commercial, retail, industrial, community, educational, healthcare,<br>accommodation and the<br>common property of<br>strata developments.</p>
    </div>
    <p class="fines-callout">Fines of<strong>up to $30,000</strong>apply for<br>non-compliance</p>
  </section>

  <!-- panel: protection -->
  <section class="panel panel-protect">
    <h2 class="right-heading">How can<span class="lead">you protect your</span>workers, contractors<br>and visitors from<br>exposure to Asbestos?</h2>
    <div class="body-copy right-copy">
      <p>You can protect your workers, contractors and visitors by exercising your Duty of Care and meeting the requirements of the current legislation to put in place an Asbestos Register and Management Plan for your building.</p>
      <p>The Asbestos Register is a document that lists all identified – or assumed – asbestos in a workplace. The person with management or control of a workplace must ensure an asbestos register is prepared and kept at the workplace and reviewed periodically.</p>
      <p class="tight">The Asbestos Management Plan helps the person with management or control of the workplace prevent exposure to airborne asbestos fibres at the workplace.</p>
    </div>
  </section>

  <svg class="foot-band" width="1200" height="26" viewBox="0 0 1200 26" aria-hidden="true">
    <rect x="0" y="2" width="1200" height="24" fill="var(--navy)"/>
    <polygon points="245,26 265,0 400,0 400,26" fill="var(--leaf-green)"/>
    <polygon points="635,26 655,0 800,0 800,26" fill="var(--leaf-green)"/>
    <polygon points="1043,26 1063,0 1200,0 1200,26" fill="var(--leaf-green)"/>
  </svg>

</main>
</body>
</html>
```